Clean and Polished Store Design

Please design a website similar to this one: http://veltrasign.com/
We require two pages:
* the home page: http://veltrasign.com/
* the product page: http://veltrasign.com/products/our-printer
Notice that there are few words and more pictures. It's clean and professional. Although I think their product page is difficult to read because it is too spread out.
Please help us generate excitement for our product via a polished and high-end looking web design. Please keep it VERY SIMPLE.
Target Market(s)
Our target market is consumers that have never bought a 3D printer before and those to whom 3D printing is new but exciting. Our market is not very technical. They love the sleek look of the printer and its ease of use.
Industry/Entity Type
Printer
Requirements
Must have
- We require two pages:
- * the home page: http://veltrasign.com/
- * the product page: http://veltrasign.com/products/our-printer
- One of our product renderings must be displayed on both the homepage and the product page.
- Our logo must be displayed on both pages.
- The pages must have a header, a footer and content equivalent to the veltrasign website.

```html
<!DOCTYPE html>
<html lang="en">
<head>
<meta charset="utf-8">
<title>Corvane 3D – Desktop 3D Printer</title>
<link rel="stylesheet" href="https://fonts.googleapis.com/css2?family=Oswald:wght@400;500&family=Roboto+Condensed:wght@300;400;700&display=swap">
<style>
:root{
  --outer:#e6e6e6;
  --page:#f0f0f0;
  --ink:#444;
  --ink-mid:#777;
  --ink-soft:#999;
  --blue:#1a9fdd;
  --blue-dark:#0b7fc0;
  --rule:#d4d4d4;
  --footer-top:#4a4a4a;
  --footer-bottom:#2b2b2b;
}
*{margin:0;padding:0;box-sizing:border-box}
html,body{width:1133px;height:1200px;overflow:hidden;background:var(--outer);font-family:"Roboto Condensed",sans-serif}
.page{position:absolute;left:101px;top:0;width:930px;height:1200px;background:var(--page);box-shadow:0 0 3px rgba(0,0,0,.35);overflow:hidden}
.abs{position:absolute}
.header{left:0;top:0;width:930px;height:117px;background:linear-gradient(#fafafa,#e4e4e4);border-bottom:1px solid var(--blue)}
.brand{left:14px;top:28px;display:flex;align-items:center;gap:12px}
.brand-name{font:700 62px/1 "Roboto Condensed",sans-serif;color:#4a4a4a;letter-spacing:-1px}
.brand-mark{width:40px;height:40px;background:#3a3a3a}
.main-nav{right:9px;top:89px;display:flex;font-size:17.5px;font-weight:700}
.main-nav a{color:var(--ink-mid);text-decoration:none;padding:4px 13px;height:28px}
.main-nav a.active{background:var(--blue);color:#fff;padding:4px 8px;margin-left:4px}
.account-nav{right:16px;top:123px;font-size:16px;font-weight:700;color:var(--ink-soft);display:flex;gap:14px;align-items:center}
.account-nav .sep{color:#bbb;font-weight:400}
.hero-photo{left:25px;top:179px;width:404px;height:338px;background:radial-gradient(ellipse 150px 140px at 45% 48%,#c8241f 0 70%,#9d1815 90%,transparent 100%),linear-gradient(#d6d6d6,#ebebeb 60%,#d9d9d9)}
.carousel-dots{left:198px;top:527px;display:flex;gap:6px;align-items:center}
.carousel-dots span{width:10px;height:10px;border-radius:50%;background:#555}
.carousel-dots span.on{width:15px;height:15px;background:#eee;border:1px solid #888}
.product-title{left:464px;top:176px;font:500 29px/1 "Oswald",sans-serif;color:var(--ink)}
.product-sub{left:464px;top:212px;font-size:16px;color:#333}
.product-copy{left:464px;top:256px;width:398px;font-size:16.5px;line-height:23.6px;color:var(--ink-soft);font-weight:300}
.spec-link{left:464px;top:496px;font-size:12.5px;color:var(--blue);text-decoration:none}
.cart-btn{left:731px;top:483px;width:128px;height:33px;background:linear-gradient(#20a8e6,var(--blue-dark));border-radius:3px;color:#fff;font-size:17px;font-weight:700;display:flex;align-items:center;justify-content:center;gap:7px}
.divider{left:0;top:562px;width:930px;border-top:1px solid var(--rule)}
.tabs{left:14px;top:581px;display:flex;gap:26px;font-size:18px;font-weight:700;color:var(--ink-mid)}
.tabs .current{color:var(--blue);border-bottom:2px solid var(--blue);position:relative;line-height:20px}
.tabs .current::after{content:"";position:absolute;left:50%;bottom:-9px;margin-left:-8px;border:8px solid transparent;border-top:7px solid var(--blue);border-bottom:0}
.sw-title{left:25px;top:622px;font:400 24px/1.2 "Oswald",sans-serif;color:var(--ink)}
.sw-sub{left:25px;top:655px;font-size:16.5px;color:#333}
.sw-list{left:25px;width:370px;font-size:15px;line-height:21.8px;color:var(--ink-mid);list-style:none;font-weight:300}
.sw-list h3{font-size:17px;font-weight:400;color:var(--blue);margin-bottom:3px}
.features{top:700px}
.compat{top:834px}
.screen{left:401px;top:627px;width:503px;height:357px;border:1px solid #aaa;border-radius:3px;background:linear-gradient(90deg,#e8e8e8 0 23%,#6fc9ec 23%,#4aa8d8 100%);box-shadow:0 1px 3px rgba(0,0,0,.25)}
.newsletter{left:0;top:1010px;width:930px;height:59px;border-top:1px solid #a9d7ef;background:linear-gradient(#f3f3f3,#e7e7e7)}
.nl-text{left:170px;top:13px;font-size:14px;color:#555;line-height:16px}
.nl-text b{font-weight:700}
.nl-field{left:435px;top:16px;width:325px;height:28px;background:#fff;border-radius:4px;border:1px solid #ddd}
.nl-btn{left:702px;top:18px;width:57px;height:24px;background:linear-gradient(#9a9a9a,#6e6e6e);border-radius:3px;color:#fff;font-size:11px;display:flex;align-items:center;justify-content:center}
.footer{left:0;top:1069px;width:930px;height:131px;background:linear-gradient(var(--footer-top),var(--footer-bottom))}
.footer-brand{left:14px;top:20px;display:flex;align-items:center;gap:10px}
.footer-brand .brand-name{font-size:40px;color:#2a2a2a}
.footer-brand .brand-mark{width:26px;height:26px;background:#222}
.search{left:14px;top:88px;width:238px;height:30px;border-radius:15px;background:#262626;color:#777;font-size:13px;display:flex;align-items:center;padding-left:12px;gap:8px}
.social{right:14px;top:15px;display:flex;gap:7px}
.social span{width:31px;height:31px;background:#3c3c3c;border-radius:3px;box-shadow:inset 0 0 0 1px #555}
.foot-links{right:14px;text-align:right;color:#999;font-size:14px}
.foot-links .s{color:#777;margin:0 4px}
</style>
</head>
<body>
<div class="page">

  <header class="abs header">
    <div class="abs brand"><span class="brand-name">Corvane 3D</span><span class="brand-mark"></span></div>
    <nav class="abs main-nav">
      <a>ABOUT</a><a>EXPLORE</a><a>CONTACT</a><a>PRESS</a><a>SUPPORT</a><a class="active">STORE</a>
    </nav>
  </header>
  <div class="abs account-nav">
    <span>LOGIN</span><span class="sep">|</span><span>ACCOUNT</span><span class="sep">|</span>
    <span>CART
      <svg width="15" height="13" viewBox="0 0 15 13"><path d="M0 1h3l2 7h8l2-5H5" fill="none" stroke="#999" stroke-width="2"/><circle cx="6" cy="11" r="1.5" fill="#999"/><circle cx="12" cy="11" r="1.5" fill="#999"/></svg>
    </span>
  </div>

  <div class="abs hero-photo" role="img" aria-label="Product rendering of a glossy red cube-shaped desktop 3D printer"></div>
  <div class="abs carousel-dots"><span></span><span class="on"></span><span></span><span></span></div>

  <h1 class="abs product-title">THE PRODUCT NAME</h1>
  <p class="abs product-sub">High Resolution Desktop 3D Printer</p>
  <p class="abs product-copy">Our high-end 3D printer offers a seamless user experience at a price affordable to the professional designer, engineer, and maker.&nbsp; The printer, software, and printing materials are all bundled in a kit that just works.&nbsp; Right out of the box.</p>
  <a class="abs spec-link">Full Tech Specs ›</a>
  <div class="abs cart-btn">Add to Cart
    <svg width="15" height="13" viewBox="0 0 15 13"><path d="M0 1h3l2 7h8l2-5H5" fill="none" stroke="#fff" stroke-width="2"/><circle cx="6" cy="11" r="1.5" fill="#fff"/><circle cx="12" cy="11" r="1.5" fill="#fff"/></svg>
  </div>

  <div class="abs divider"></div>
  <nav class="abs tabs"><span>OVERVIEW</span><span>FEATURES</span><span class="current">SOFTWARE</span><span>SPECIFICATIONS</span><span>MATERIAL</span></nav>

  <h2 class="abs sw-title">Corvane 3D Software</h2>
  <p class="abs sw-sub">Easily import your .STL files and make them real.</p>
  <ul class="abs sw-list features">
    <h3>Software Features:</h3>
    <li>• Intuitive workflow to simplify job setup</li>
    <li>• Auto-Orient optimizes part rotation for support generation</li>
    <li>• Manual tools for rotation, scaling, and duplication</li>
    <li>• Analyze individual print layers with 3D stage view</li>
  </ul>
  <ul class="abs sw-list compat">
    <h3>Software Compatibility:</h3>
    <li>• Panelix 8 / Lumen / Horizon</li>
    <li>• Orchard OS</li>
  </ul>
  <div class="abs screen" role="img" aria-label="Screenshot of the print preparation software showing a green octopus model on a blue build platform"></div>

  <section class="abs newsletter">
    <p class="abs nl-text"><b>SIGN UP FOR OUR NEWSLETTER:</b><br>We'll let you know about important updates.</p>
    <div class="abs nl-field"></div>
    <div class="abs nl-btn">Sign Up</div>
  </section>

  <footer class="abs footer">
    <div class="abs footer-brand"><span class="brand-name">Corvane 3D</span><span class="brand-mark"></span></div>
    <div class="abs search">
      <svg width="11" height="11" viewBox="0 0 11 11"><circle cx="4.5" cy="4.5" r="3.3" fill="none" stroke="#888" stroke-width="1.6"/><path d="M7 7l3.3 3.3" stroke="#888" stroke-width="1.8"/></svg>Search...
    </div>
    <div class="abs social"><span></span><span></span><span></span><span></span><span></span></div>
    <p class="abs foot-links" style="top:56px">ABOUT<span class="s">|</span>EXPLORE<span class="s">|</span>CONTACT<span class="s">|</span>PRESS<span class="s">|</span>STORE</p>
    <p class="abs foot-links" style="top:79px">Terms of Service<span class="s">|</span>Privacy Policy<span class="s">|</span>Sales &amp; Returns</p>
    <p class="abs foot-links" style="top:104px">© 2013&nbsp; Corvane 3D.&nbsp; All Rights Reserved.</p>
  </footer>
</div>
</body>
</html>
```